Express envelope design for courier company

We're a courier company launching a new service for sending documents around Australia. We need a design for the express envelope that will be used to hold the documents during transit. The envelope will be printed in colour on cardboard. Please see brief attached.

Design cues:
• Vibrant
• Simplified
• Clean
• Aesthetically pleasing
• Artistic
• Nothing “institutional” or “Harwick Lines”
• Nothing cramped, no small text

It's fine to crop, recolour, or reinterpret the logo.

Industry/Entity Type

It Company

Font styles to use
Sans Serif

Requirements
Must have
• Dimensions:
• Back side: 350 x 230 mm
• Front side: 387.5 x 230 mm (including flap to close envelope)
• Back side barcode panel: 90 x 75 mm (blank area for adhesive barcode)
• Back side address panel: 150 x 90 mm (see PDF for contents and layout)
• Front side text:
• QM-DR
• Express Envelope
• Send With Trust
• 1300 584 961
• qmdr.com.au
• Back side text:
• For documents
• Max. weight 500g, max width 20mm
• Send With Trust
• • Time-guaranteed and next-flight-out service for vital deliveries
• • Same-day and next-day local services
• • Overnight service to most Australian locations
• • Budget road service Australia-wide
• • Worldwide express courier
• Visit qmdr.com.au or phone 1300 584 961
• Flap text:
• Go to qmdr.com.au to book your pickup.
• Carried subject to QM-DR Standard Conditions of Carriage; see our website.
Nice to have
• Our web colours:
• #fcd614
• #d06517
• #3b5274
• #f0f0d8
• #382a3a

```html
<!DOCTYPE html>
<html lang="en">
<head>
<meta charset="utf-8">
<title>QM-DR Express Envelope – Front Open</title>
<link rel="stylesheet" href="https://fonts.googleapis.com/css2?family=Arimo:ital,wght@0,400;0,700;1,400;1,700&display=swap">
<style>
  :root {
    --paper: #ffffff;
    --envelope-yellow: #fdd400;
    --navy: #004a80;
    --orange: #ff5a00;
    --orange-light: #ff9a00;
    --white: #ffffff;
    --caption: #333333;
  }
  html, body {
    margin: 0;
    padding: 0;
    width: 1200px;
    height: 1000px;
    overflow: hidden;
    background: var(--paper);
  }
  .artboard {
    display: block;
    width: 1200px;
    height: 1000px;
    font-family: "Arimo", Arial, sans-serif;
  }
  .envelope-body { fill: var(--envelope-yellow); }
  .navy-fill { fill: var(--navy); }
  .brand-name { fill: var(--white); font-weight: 700; font-size: 58px; }
  .slogan { fill: var(--white); font-weight: 700; font-style: italic; font-size: 37px; }
  .product-title { fill: var(--orange); font-weight: 700; font-style: italic; font-size: 58px; }
  .footer-contact { fill: var(--white); font-style: italic; font-size: 22px; }
  .flap-headline { fill: var(--white); font-style: italic; font-size: 22px; }
  .flap-terms { fill: var(--white); font-style: italic; font-size: 13.5px; }
  .view-caption { fill: var(--caption); font-size: 21px; }
</style>
</head>
<body>
<svg class="artboard" viewBox="0 0 1200 1000" xmlns="http://www.w3.org/2000/svg">
  <defs>
    <linearGradient id="orangeStreak" x1="255" y1="0" x2="1016" y2="0" gradientUnits="userSpaceOnUse">
      <stop offset="0" stop-color="#ff9a00" stop-opacity="0"/>
      <stop offset="0.25" stop-color="#ff7a00" stop-opacity="0.9"/>
      <stop offset="1" stop-color="#ff5a00"/>
    </linearGradient>
    <linearGradient id="brandBandFade" x1="210" y1="0" x2="505" y2="0" gradientUnits="userSpaceOnUse">
      <stop offset="0" stop-color="#2a4a6e" stop-opacity="0"/>
      <stop offset="0.12" stop-color="#2a4a6e"/>
      <stop offset="0.88" stop-color="#2a4a6e"/>
      <stop offset="1" stop-color="#2a4a6e" stop-opacity="0"/>
    </linearGradient>
  </defs>

  <!-- envelope front -->
  <g class="envelope-front">
    <rect class="envelope-body" x="83" y="243" width="933" height="613"/>

    <!-- navy speed stripes -->
    <g class="navy-stripes navy-fill">
      <rect x="83" y="374" width="933" height="8"/>
      <rect x="83" y="386" width="933" height="1.5"/>
      <rect x="83" y="403" width="933" height="8"/>
      <rect x="83" y="427" width="933" height="1.5"/>
      <rect x="83" y="433" width="933" height="10"/>
    </g>

    <!-- brand name band -->
    <g class="brand-lockup">
      <rect x="210" y="374" width="295" height="69" fill="url(#brandBandFade)"/>
      <text class="brand-name" x="365" y="429" text-anchor="middle">QM-DR</text>
    </g>

    <text class="slogan" x="985" y="363" text-anchor="end">Ship With Trust</text>

    <text class="product-title" x="990" y="678" text-anchor="end">Express Envelope</text>

    <!-- orange speed stripes -->
    <g class="orange-stripes" fill="url(#orangeStreak)">
      <rect x="255" y="692" width="761" height="6"/>
      <rect x="255" y="703" width="761" height="1.5"/>
      <rect x="255" y="718" width="761" height="7"/>
      <rect x="255" y="741" width="761" height="1.5"/>
      <rect x="255" y="746" width="761" height="10"/>
    </g>

    <!-- footer contact bar -->
    <rect class="navy-fill" x="83" y="815" width="933" height="41"/>
    <text class="footer-contact" x="550" y="842" text-anchor="middle">Visit qmdr.com.au or phone 1300 584 961</text>
  </g>

  <!-- closing flap -->
  <g class="envelope-flap">
    <path class="navy-fill" d="M1016 243 H1100 Q1116 244 1116 258 V840 Q1116 853 1100 854 L1016 856 Z"/>
    <text class="flap-headline" transform="translate(1063 550) rotate(-90)" text-anchor="middle">Go to qmdr.com.au to book your pickup.</text>
    <text class="flap-terms" transform="translate(1085 550) rotate(-90)" text-anchor="middle">Carried subject to QM-DR Standard Conditions of Carriage; see our website.</text>
  </g>

  <text class="view-caption" x="600" y="918" text-anchor="middle">front - open</text>
</svg>
</body>
</html>
```